I am a highly experienced private practice psychotherapist serving high end clientele in the Wall Street area of New York City. I need electronic letterhead (that can also be printed) to use for bills, receipts, and correspondences.

My clients are very high end and are used to elegance and wealth. The letterhead should contain the following information: Marian T. Holcombe, LCSW 72 Pellham Street, Suite 2561 New York, NY 10087 Phone : (917) 555-3194 email: therapy@marianholcombelcsw.example website: www.marianholcombelcsw.example

Thank you for your designs. Please be advised that the letterhead will be used for bills/invoices; professional letters to other mental health professionals and doctors, as well as to attorneys. It needs to be highly professional in the same way that a law firm has professional and elegant letterhead, raher than whimsical or with spa designers. My letters end up as official documents.

```html
<!DOCTYPE html>
<html lang="en">
<head>
<meta charset="utf-8">
<title>Marian T. Holcombe, LCSW — Letterhead</title>
<link rel="stylesheet" href="https://fonts.googleapis.com/css2?family=Open+Sans:wght@400;700&display=swap">
<style>
  :root {
    --gold-light: #f2c96c;
    --gold-deep: #e3ad45;
    --blue-light: #6bb6e8;
    --blue-mid: #0f74bf;
    --blue-deep: #0b4c9e;
    --paper: #ffffff;
    --ink-light: #ffffff;
  }
  html, body {
    margin: 0;
    padding: 0;
    overflow: hidden;
  }
  body {
    width: 933px;
    height: 1200px;
  }
  .letterhead {
    position: relative;
    width: 933px;
    height: 1200px;
    overflow: hidden;
    background: linear-gradient(135deg, var(--gold-light), var(--gold-deep) 50%, var(--gold-light));
    font-family: "Open Sans", Arial, sans-serif;
  }
  .letterhead__art {
    position: absolute;
    inset: 0;
    width: 933px;
    height: 1200px;
    display: block;
  }
  .letterhead__name {
    position: absolute;
    left: 47px;
    top: 52px;
    margin: 0;
    font-size: 29px;
    font-weight: 400;
    color: var(--ink-light);
    letter-spacing: 0.2px;
    white-space: nowrap;
  }
  .letterhead__contact {
    position: absolute;
    left: 25px;
    top: 1157px;
    margin: 0;
    font-size: 11px;
    color: var(--ink-light);
    white-space: nowrap;
    letter-spacing: -0.1px;
  }
  .contact__label {
    font-weight: 700;
  }
  .contact__item {
    margin-right: 4px;
  }
</style>
</head>
<body>
<div class="letterhead">
  <svg class="letterhead__art" viewBox="0 0 630 810" preserveAspectRatio="none" aria-hidden="true">
    <defs>
      <linearGradient id="band-blue" x1="0" y1="0" x2="1" y2="0">
        <stop offset="0" stop-color="var(--blue-light)"/>
        <stop offset="0.55" stop-color="var(--blue-mid)"/>
        <stop offset="1" stop-color="var(--blue-deep)"/>
      </linearGradient>
    </defs>
    <rect class="page" x="8" y="8" width="614" height="792" fill="var(--paper)"/>
    <path class="band-top" d="M8 8 H622 V44 C540 46 450 52 360 66 C250 84 120 100 8 105 Z" fill="url(#band-blue)"/>
    <path class="band-bottom" d="M8 766 C140 760 270 748 390 728 C480 713 560 704 622 700 V800 H8 Z" fill="url(#band-blue)"/>
  </svg>

  <h1 class="letterhead__name">Marian T. Holcombe, LCSW</h1>

  <p class="letterhead__contact">
    <span class="contact__item"><span class="contact__label">Phone:</span> (917) 555-3194</span>
    <span class="contact__item"><span class="contact__label">E-mail:</span> therapy@marianholcombelcsw.example</span>
    <span class="contact__item"><span class="contact__label">Web:</span> www.marianholcombelcsw.example</span>
    <span class="contact__item"><span class="contact__label">Address:</span> 72 Pellham Street, Suite 2561 New York, NY 10087</span>
  </p>
</div>
</body>
</html>
```